Need a clean & modern homepage for an education site + opportunity for longer term work

Thanks for viewing our project. We are excited about this new website and we hope that we might build a relationship with designers as we work on this project. I provided quite a few details and requirements to help you more quickly create a design that meets our needs.
Who we are:
We are a website that discusses the importance of college accreditation and provides a directory of college programs.
What we need:
A homepage that meets the below requirements and is inspired by the examples provided
Definition of accredited:
ac·cred·it·ed [uh-kred-i-tid] adj.
1. officially recognized as meeting the essential requirements, as of academic excellence: accredited schools.
2. provided with official credentials, as by a government: an accredited diplomatic representative.
3. accepted as authoritative: an accredited theory.
Overall look and feel for the homepage:
- Clean, simple and modern
- Limited (or zero) pictures
- Utilize color blocks with text
- A trend seems to be longer vertical length homepages with lots of whitespace. I generally like this trend as long as the page is not way to tall.
Inspirations: Sites that have a similar look and feel to what I need.
http://plinvar.org/
http://www.tumbrelstat.com/colleges/harrowgate-university/
http://quietmarble.org/
http://www.vellichorstaffing.com/
http://www.plonk.com/
http://sketches.zimvo.com/
Items to be included on the homepage. Details below on each item.
- Top navigation
- Logo: Please leave a blank area for a logo. The logo has not been designed.
- Simple graphic/color block at the top that highlights a definition of “Accredited” – the definition should be formatted like it is being copy/pasted from a dictionary.
- Space for a video and small (50 word) written description of the video. You can use placeholder text.
- One section with 3 Paragraphs of content (each paragraph around 100 words) with a header at the top. You can use placeholder text but please create the formatting. At the end of the 3 paragraphs please have a “Read More” Note this shouldn't be 3 separate paragraphs with three read mores - it is 3 paragraphs with one read more at the end.
- An area with the header “Search Colleges by State” that has anchor text links to all 50 states.
Top navigation:
- Home
- States – with a subnav dropdown that includes all 50 US states.
- Programs – with a subnav dropdown that includes program titles (list below)
- Degrees - with a subnav dropdown that includes 5 degree levels (list below)
- Accreditation – no subnav
- Rankings – no subnav
- Resources – no subnav
Footer
- Link to about us, privacy, and a copyright www.url.com
Programs List for sub navigation
Accounting
Art
Bible
Business
Criminal Justice
Design
Engineering
English
Law
LPN to RN
Management
Math
MBA
MPH
Medical Assisting
Military
Nursing
Occupational Therapy
Paralegal
Psychology
Pharmacy
RN to BSN
Radiology
Social Work
Sonography
Degrees list for sub navigation
Certificate
Associate
Bachelors
Masters
PhD
Thanks so much - looking forward to working with you!

```html
<!DOCTYPE html>
<html lang="en">
<head>
<meta charset="utf-8">
<title>Accredited — Homepage</title>
<link rel="stylesheet" href="https://fonts.googleapis.com/css2?family=Titillium+Web:wght@300;400;600&family=Source+Sans+3:wght@400;600&display=swap">
<style>
  :root{
    --orange:#f47a20;
    --orange-dark:#d9600c;
    --blue:#27a7d3;
    --green:#8bb811;
    --red:#ef4433;
    --ink:#333;
    --grey:#8a8a8a;
    --grey-light:#bdbdbd;
    --band:#f4f4f4;
    --white:#fff;
  }
  *{box-sizing:border-box;margin:0;padding:0}
  html,body{width:673px;height:1200px;overflow:hidden;background:var(--white)}
  body{position:relative;font-family:"Source Sans 3",Arial,sans-serif;color:var(--ink)}
  .abs{position:absolute}
  .center{left:0;width:673px;text-align:center}

  /* navigation */
  .topnav{position:absolute;top:0;left:0;width:673px;height:37px;background:var(--orange)}
  .topnav a{position:absolute;top:0;height:37px;line-height:38px;color:var(--white);text-decoration:none;
    font-family:"Titillium Web",sans-serif;font-size:12px;transform:translateX(-50%);white-space:nowrap}
  .topnav .home{left:37px;width:65px;transform:none;text-align:center;background:var(--orange-dark)}
  .topnav .sep{position:absolute;top:0;width:1px;height:37px;background:rgba(255,255,255,.35)}

  .logo{left:41px;top:54px;font-family:"Titillium Web",sans-serif;font-weight:400;font-size:30px;color:#222}
  .social{left:546px;top:69px;display:flex;gap:3px}
  .social span{width:19px;height:19px;border-radius:50%;background:var(--orange)}

  /* hero */
  .hero{left:0;top:106px;width:673px;height:250px;
    background:linear-gradient(90deg,#6f8a4a 0%,#a48a6e 18%,#5b4a3c 40%,#7a5e48 60%,#3f3a33 78%,#8fae5e 100%)}
  .hero-panel{left:136px;top:168px;width:398px;height:146px;background:rgba(30,30,30,.62)}
  .hero-title{left:136px;width:398px;top:174px;text-align:center;font-family:"Titillium Web",sans-serif;
    font-weight:300;font-size:29px;color:var(--white)}
  .hero-sub{left:136px;width:398px;top:210px;text-align:center;font-size:9.5px;line-height:13px;color:#eee}
  .field{background:var(--white);border-radius:2px;font-size:10px;color:#444;padding-left:9px;display:flex;align-items:center}
  .field svg{position:absolute;right:6px}
  .arrow-btn{width:30px;height:30px;border-radius:50%;background:rgba(255,255,255,.85);display:flex;align-items:center;justify-content:center}

  /* definition */
  .def-word{top:384px;font-family:"Titillium Web",sans-serif;font-size:18px;font-weight:600;color:var(--orange)}
  .def-text{top:410px;font-size:11.5px;color:#555}

  .band{left:0;top:430px;width:673px;height:410px}

  /* feature blocks */
  .block{top:455px;width:194px;height:114px;color:var(--white)}
  .block h3{position:absolute;left:16px;top:10px;font-family:"Titillium Web",sans-serif;font-weight:400;font-size:14.5px}
  .block p{position:absolute;left:71px;top:34px;width:118px;font-size:8px;line-height:13px}
  .block .more{position:absolute;left:71px;top:89px;font-size:8.5px;font-weight:600}
  .block svg{position:absolute;left:20px;top:38px}
  .b-blue{left:36px;background:var(--blue)}
  .b-green{left:239px;background:var(--green)}
  .b-red{left:442px;background:var(--red)}

  /* video */
  .video-frame{left:53px;top:638px;width:245px;height:152px;background:var(--white);border:1px solid #e2e2e2}
  .video-still{left:58px;top:644px;width:235px;height:141px;background:linear-gradient(120deg,#8fa6b8,#c9b59a 45%,#6a7f95)}
  .play{left:161px;top:699px;width:30px;height:30px;border-radius:50%;background:#222;border:2px solid #fff;display:flex;align-items:center;justify-content:center}
  .video-title{left:353px;top:640px;font-family:"Titillium Web",sans-serif;font-weight:400;font-size:22px;color:var(--orange)}
  .video-copy{left:354px;width:280px;font-size:8.6px;line-height:13px;color:#777}
  .btn-dark{left:355px;top:764px;width:66px;height:18px;background:#333;color:var(--white);font-size:8px;font-weight:600;
    display:flex;align-items:center;justify-content:center;border-radius:2px}

  /* services */
  .services-title{top:874px;font-family:"Titillium Web",sans-serif;font-size:19.5px;color:#333}
  .services-intro{top:903px;left:90px;width:493px;text-align:center;font-size:8px;line-height:12px;color:#888}
  .service{top:946px;width:150px;text-align:center}
  .service .disc{width:66px;height:66px;border-radius:50%;margin:0 auto;display:flex;align-items:center;justify-content:center}
  .service h4{margin-top:7px;font-weight:400;font-size:10.5px;color:#444}
  .service p{margin-top:2px;font-size:8px;line-height:12px;color:#999}
  .service .learn{display:block;margin-top:3px;font-size:8px;font-weight:600}
  .o .disc{background:var(--orange)} .o .learn{color:var(--orange)}
  .b .disc{background:var(--blue)} .b .learn{color:var(--blue)}

  /* footer */
  .footer-rule{left:0;top:1118px;width:673px;height:1px;background:#ddd}
  .footer-links{left:35px;top:1141px;font-size:10.5px;color:#444}
  .footer-links i{font-style:normal;margin:0 5px;color:#666}
  .copyright{left:36px;top:1164px;font-size:7.5px;color:#666}
</style>
</head>
<body>

<nav class="topnav">
  <a class="home" href="#">HOME</a>
  <a href="#" style="left:138px">STATES</a>
  <a href="#" style="left:219px">PROGRAMS</a>
  <a href="#" style="left:305px">DEGREES</a>
  <a href="#" style="left:402px">ACCREDITATION</a>
  <a href="#" style="left:504px">RANKINGS</a>
  <a href="#" style="left:594px">RESOURCES</a>
  <span class="sep" style="left:172px"></span>
  <span class="sep" style="left:265px"></span>
  <span class="sep" style="left:342px"></span>
  <span class="sep" style="left:461px"></span>
  <span class="sep" style="left:548px"></span>
</nav>

<div class="abs logo">Accredited</div>
<div class="abs social" aria-label="Social links"><span></span><span></span><span></span><span></span></div>

<section>
  <div class="abs hero" role="img" aria-label="Photo of a group of college students sitting together outdoors on campus"></div>
  <div class="abs hero-panel"></div>
  <h1 class="abs hero-title">Search Colleges by State</h1>
  <p class="abs hero-sub">Mauris vel lacus vitae felis vestibulum volutpat. Etiam est nunc, venenatis<br>in, tristique eu, imperdiet ac, nisl Cum sociis natoque</p>
  <div class="abs field" style="left:202px;top:242px;width:279px;height:25px;font-size:10.5px">type your state here
    <svg width="16" height="16" viewBox="0 0 16 16"><circle cx="7" cy="7" r="5" fill="none" stroke="#aaa" stroke-width="1.6"/><line x1="11" y1="11" x2="15" y2="15" stroke="#aaa" stroke-width="1.8"/></svg></div>
  <div class="abs field" style="left:203px;top:272px;width:137px;height:22px;font-size:8.5px">By program
    <svg width="14" height="14" viewBox="0 0 16 16"><circle cx="7" cy="7" r="5" fill="none" stroke="#aaa" stroke-width="1.6"/><line x1="11" y1="11" x2="15" y2="15" stroke="#aaa" stroke-width="1.8"/></svg></div>
  <div class="abs field" style="left:345px;top:272px;width:136px;height:22px;font-size:8.5px">by degree
    <svg width="14" height="14" viewBox="0 0 16 16"><circle cx="7" cy="7" r="5" fill="none" stroke="#aaa" stroke-width="1.6"/><line x1="11" y1="11" x2="15" y2="15" stroke="#aaa" stroke-width="1.8"/></svg></div>
  <div class="abs arrow-btn" style="left:19px;top:217px"><svg width="10" height="12" viewBox="0 0 10 12"><polyline points="7,1 2,6 7,11" fill="none" stroke="#333" stroke-width="1.6"/></svg></div>
  <div class="abs arrow-btn" style="left:627px;top:217px"><svg width="10" height="12" viewBox="0 0 10 12"><polyline points="3,1 8,6 3,11" fill="none" stroke="#333" stroke-width="1.6"/></svg></div>
</section>

<svg class="abs band" viewBox="0 0 673 410" aria-hidden="true">
  <defs><linearGradient id="bandFade" x1="0" y1="0" x2="0" y2="1">
    <stop offset="0" stop-color="#fff"/><stop offset=".35" stop-color="#f5f5f5"/><stop offset="1" stop-color="#f4f4f4"/></linearGradient></defs>
  <path d="M0 0H673V410H0Z" fill="url(#bandFade)"/>
  <path d="M0 165H318Q342 165 342 195Q342 165 366 165H673V0H0Z" fill="#fff" opacity=".0"/>
  <path d="M0 165H310Q340 165 342 195Q344 165 374 165H673V160H0Z" fill="#fff"/>
  <path d="M0 402H310Q340 402 342 372Q344 402 374 402H673V410H0Z" fill="#fff"/>
</svg>

<section>
  <h2 class="abs center def-word">ac·cred·it·ed [uh-kred-i-tid] adj</h2>
  <p class="abs center def-text">officially recognized as meeting the essential requirements, as of academic excellence: accredited schools.</p>
</section>

<section>
  <article class="abs block b-blue">
    <h3>Our Programs</h3>
    <svg width="40" height="40" viewBox="0 0 40 40"><path d="M5 4H35L38 14H2Z M4 14V36H36V14 M14 36V22H26V36" fill="none" stroke="#fff" stroke-width="2.2" stroke-linejoin="round"/><path d="M10 4L8 14M16 4L15 14M24 4L25 14M30 4L32 14" stroke="#fff" stroke-width="1.6"/></svg>
    <p>Mauris vel lacus vitae felis ves-tibulum volutpat. Etiam est nunc, venenatis in, tristique eu, imperdiet ac, nisl.</p>
    <span class="more">Read More ▸</span>
  </article>
  <article class="abs block b-green">
    <h3>How it Works</h3>
    <svg width="40" height="40" viewBox="0 0 40 40"><path d="M28 4L36 12L13 35L3 37L5 27Z M24 8L32 16 M5 27L13 35" fill="none" stroke="#fff" stroke-width="2.2" stroke-linejoin="round"/></svg>
    <p>Mauris vel lacus vitae felis ves-tibulum volutpat. Etiam est nunc, venenatis in, tristique eu, imperdiet ac, nisl.</p>
    <span class="more">Read More ▸</span>
  </article>
  <article class="abs block b-red">
    <h3>Why Us?</h3>
    <svg width="40" height="40" viewBox="0 0 40 40"><path d="M14 26C10 22 8 19 8 15A12 12 0 0 1 32 15C32 19 30 22 26 26V30H14Z M14 33H26 M16 37H24" fill="none" stroke="#fff" stroke-width="2.2" stroke-linejoin="round"/></svg>
    <p>Mauris vel lacus vitae felis ves-tibulum volutpat. Etiam est nunc, venenatis in, tristique eu, imperdiet ac, nisl.</p>
    <span class="more">Read More ▸</span>
  </article>
</section>

<section>
  <div class="abs video-frame"></div>
  <div class="abs video-still" role="img" aria-label="Video still of students writing at desks in a classroom"></div>
  <div class="abs play"><svg width="10" height="12" viewBox="0 0 10 12"><path d="M1 0L10 6L1 12Z" fill="#fff"/></svg></div>
  <h2 class="abs video-title">Watch Our Video</h2>
  <p class="abs video-copy" style="top:671px">Mauris vel lacus vitae felis vestibulum volutpat. Etiam est nunc, venenatis in, tristique eu, imperdiet ac, nisl. Cum sociis natoque penatibus et magnis dis parturient montes</p>
  <p class="abs video-copy" style="top:716px">Class aptent taciti sociosqu ad litora torquent per conubia nostra, per inceptos hymenaeos. Proin nulla arcu, nonummy luctus, dictum eget, fermentum et, lorem.</p>
  <div class="abs btn-dark">VIEW MORE</div>
</section>

<section>
  <h2 class="abs center services-title">Featured Services Provide</h2>
  <p class="abs services-intro">Phasellus felis dolor, scelerisque a, tempus eget, lobortis id, libero. Donec scelerisque leo ac risus. Praesent sit amet est. In dictum, dolor eu dictum porttitor, enim felis viverra mi, eget luctus massa purus quis odio. Etiam nulla massa, pharetra facilisis, volutpat in</p>

  <div class="abs service o" style="left:35px">
    <div class="disc"><svg width="40" height="30" viewBox="0 0 40 30" fill="#fff"><circle cx="8" cy="7" r="4"/><circle cx="20" cy="5" r="4.5"/><circle cx="32" cy="7" r="4"/><rect x="2" y="13" width="12" height="14" rx="3"/><rect x="14" y="11" width="12" height="17" rx="3"/><rect x="26" y="13" width="12" height="14" rx="3"/></svg></div>
    <h4>Community</h4>
    <p>Phasellus felis dolor, scelerisque a, tempus eget, lobortis id, libero. Donec scelerisque leo ac risus Praesent sit</p>
    <span class="learn">LEARN MORE</span>
  </div>
  <div class="abs service b" style="left:184px">
    <div class="disc"><svg width="40" height="28" viewBox="0 0 40 28"><rect x="7" y="2" width="26" height="18" rx="1.5" fill="none" stroke="#fff" stroke-width="2.2"/><path d="M2 23H38L36 26H4Z" fill="#fff"/></svg></div>
    <h4>Onlines Access</h4>
    <p>Phasellus felis dolor, scelerisque a, tempus eget, lobortis id, libero. Donec scelerisque leo ac risus Praesent sit</p>
    <span class="learn">LEARN MORE</span>
  </div>
  <div class="abs service o" style="left:339px">
    <div class="disc"><svg width="34" height="38" viewBox="0 0 34 38"><path d="M9 8H25V36H9Z M2 16H9V36H2Z M25 16H32V36H25Z M13 4H21V8H13Z M17 0V4" fill="none" stroke="#fff" stroke-width="2"/><g fill="#fff"><rect x="12" y="12" width="3" height="3"/><rect x="19" y="12" width="3" height="3"/><rect x="12" y="18" width="3" height="3"/><rect x="19" y="18" width="3" height="3"/><rect x="12" y="24" width="3" height="3"/><rect x="19" y="24" width="3" height="3"/><rect x="4" y="20" width="3" height="3"/><rect x="27" y="20" width="3" height="3"/><rect x="15" y="30" width="4" height="6"/></g></svg></div>
    <h4>High Schools</h4>
    <p>Phasellus felis dolor, scelerisque a, tempus eget, lobortis id, libero. Donec scelerisque leo ac risus Praesent sit</p>
    <span class="learn">LEARN MORE</span>
  </div>
  <div class="abs service b" style="left:493px">
    <div class="disc"><svg width="38" height="32" viewBox="0 0 38 32" fill="#fff"><circle cx="13" cy="9" r="7"/><path d="M0 31C0 22 5 18 13 18C21 18 26 22 26 31Z"/><circle cx="26" cy="8" r="6" opacity=".85"/><path d="M27 16C33 16 38 20 38 28H28C28 23 26 19 23 17Z" opacity=".85"/></svg></div>
    <h4>Students &amp; Staff</h4>
    <p>Phasellus felis dolor, scelerisque a, tempus eget, lobortis id, libero. Donec scelerisque leo ac risus Praesent sit</p>
    <span class="learn">LEARN MORE</span>
  </div>
</section>

<footer>
  <div class="abs footer-rule"></div>
  <div class="abs footer-links">Home<i>|</i>States<i>|</i>Programs<i>|</i>Degrees<i>|</i>Accreditation<i>|</i>Rankings<i>|</i>Resources</div>
  <div class="abs copyright">© 2013 Company Name.&nbsp; All right reserved.&nbsp; Term of Use</div>
</footer>

</body>
</html>
```